New Health Business Needs Flyer for Africa

We are a new network marketing company about to launch in Africa. I need a flyer made purely for the business and earning opportunity that people can get with our company. This is a home based business that anyone can get involved with. Very low start up costs with high quality effective and innovative products. You can visit our blog to get more information on the benefits I would like to see on the flyer. http://tolvenpost.example. This flyer is to attract people who want to earn more money and build a long term business with financial security.
Updates

This needs to be about making more money. Luxury lifestyle, flash cars, big houses etc. I don't want anything about the product on this flyer

Reason: to give you all a bit more time on this I have extended the time period

Reason: to give you more time

Target Market(s)

anyone who wants to earn more money. Over 18 years old.

Industry/Entity Type

Marketing

Requirements
Must have
• This is a simple handout flyer A5 size. Can have front and back. Because we are opening in Africa, any faces or people should be black. It should have the logo which is uploaded to files also.

```html
<!DOCTYPE html>
<html lang="en">
<head>
<meta charset="utf-8">
<title>Solvantra International – Business Opportunity Flyer</title>
<link rel="stylesheet" href="https://fonts.googleapis.com/css2?family=Poppins:ital,wght@0,400;0,600;1,600&display=swap">
<style>
  :root {
    --page: #ffffff;
    --sheet-top: #f4f4f4;
    --sheet-bottom: #d9d9d9;
    --green: #2ee62e;
    --blue: #1a3cf5;
    --grey-text: #4a4a4a;
    --photo-sky: #8fd3ef;
    --photo-mid: #c9a48c;
    --photo-ground: #7ea85a;
  }
  * { margin: 0; padding: 0; box-sizing: border-box; }
  html, body {
    width: 916px; height: 1200px; overflow: hidden;
    background: var(--page);
    font-family: "Poppins", sans-serif;
  }
  .flyer {
    position: absolute; left: 156px; top: 118px;
    width: 650px; height: 920px; overflow: hidden;
    background: linear-gradient(180deg, var(--sheet-top) 0%, #ececec 50%, var(--sheet-bottom) 100%);
    box-shadow: 0 18px 50px rgba(0,0,0,0.18);
  }
  .hero { position: absolute; left: 0; top: 0; width: 650px; height: 400px; }
  .brand {
    position: absolute; left: 22px; top: 374px;
    display: flex; align-items: center; gap: 12px;
  }
  .brand-dot { width: 22px; height: 22px; border-radius: 50%; background: var(--green); }
  .brand-name {
    font-size: 52px; font-weight: 600; color: var(--blue); line-height: 1; letter-spacing: -1px;
  }
  .brand-sub {
    position: absolute; left: 188px; top: 424px;
    font-size: 19px; font-weight: 400; color: var(--blue);
  }
  .headline {
    position: absolute; left: 24px; top: 450px;
    font-size: 37px; font-weight: 600; line-height: 45px; color: var(--green);
    letter-spacing: -0.3px;
  }
  .benefits { position: absolute; left: 48px; top: 552px; list-style: none; }
  .benefits li {
    position: relative; padding-left: 22px;
    font-size: 23px; font-weight: 600; color: var(--blue); line-height: 37px;
  }
  .benefits li::before {
    content: ""; position: absolute; left: 4px; top: 14px;
    width: 8px; height: 12px; border-radius: 50% 50% 50% 0;
    background: var(--green); transform: rotate(-20deg);
  }
  .cta {
    position: absolute; left: 34px; top: 786px;
    font-size: 19px; font-weight: 600; font-style: italic; color: var(--grey-text);
  }
  .pointer { position: absolute; left: 90px; top: 816px; }
  .contact-box {
    position: absolute; left: 157px; top: 815px; width: 470px; height: 84px;
    border: 1.5px solid var(--green); border-radius: 14px; background: #fff;
    padding: 12px 14px 0 15px;
  }
  .contact-row {
    display: flex; align-items: baseline; gap: 6px;
    font-size: 14px; color: var(--blue); line-height: 21px;
  }
  .contact-row .fill { flex: 1; border-bottom: 1.5px dotted var(--blue); transform: translateY(-3px); }
</style>
</head>
<body>
  <main class="flyer">
    <svg class="hero" viewBox="0 0 650 400" aria-hidden="false">
      <defs>
        <linearGradient id="photoTones" x1="0" y1="0" x2="0.4" y2="1">
          <stop offset="0" stop-color="var(--photo-sky)"/>
          <stop offset="0.5" stop-color="var(--photo-mid)"/>
          <stop offset="1" stop-color="var(--photo-ground)"/>
        </linearGradient>
      </defs>
      <path role="img" aria-label="Lifestyle collage: luxury watch, tropical beach, large house with palm trees, smiling woman holding car keys beside a white car"
            d="M106 0 H650 V352 C560 372 480 384 420 382 C300 378 200 330 150 240 C120 170 104 80 106 0 Z"
            fill="url(#photoTones)"/>
      <path d="M106 0 C104 80 120 170 150 240 C200 330 300 378 420 382 C480 384 560 372 650 352"
            fill="none" stroke="var(--green)" stroke-width="5"/>
    </svg>

    <div class="brand">
      <span class="brand-dot"></span>
      <span class="brand-name">Solvantra</span>
    </div>
    <div class="brand-sub">international</div>

    <h1 class="headline">The Most Lucrative Business<br>Opportunity In Africa Today!</h1>

    <ul class="benefits">
      <li>Life Changing Products</li>
      <li>5 Levels Of Fast Start Bonuses</li>
      <li>5 Levels Of Matching Bonuses</li>
      <li>Fully Paid Up Car Bonus</li>
      <li>Valcourt Bonus</li>
      <li>Loyalty Bonuses Up To $1 Million</li>
    </ul>

    <p class="cta">Contact Me Now For Top Positioning</p>

    <svg class="pointer" width="70" height="60" viewBox="0 0 70 60" aria-hidden="true">
      <path d="M4 2 V48 H58" fill="none" stroke="var(--grey-text)" stroke-width="2.5"/>
      <path d="M56 42 L66 48 L56 54 Z" fill="var(--grey-text)"/>
    </svg>

    <section class="contact-box">
      <div class="contact-row"><span>NAME</span><span class="fill"></span></div>
      <div class="contact-row"><span>TELEPHONE</span><span class="fill"></span></div>
      <div class="contact-row"><span>WEBSITE URL</span><span class="fill"></span></div>
    </section>
  </main>
</body>
</html>
```